Name Card Design - CuiFeng Enterprise Pte Ltd

Family office operations base in Singapore that deals with financial investments and trading. Company name is direct english translation of Chinese characters 翠枫 (meaning overflowing/surplus + stable as mountain)。We do not have a company logo design yet. Was considering having the logo as traditional chinese seal design. Other ideas are welcomed.

Target Market(s)

financial institutions, investors, networking

Industry/Entity Type

Finance

Contact Information for Business Card

Pls use fictitious names and contact details in design

Requirements
Must have
• Logo, Name, Title, Address, Email, Tel, Mobile

```html
<!DOCTYPE html>
<html lang="en">
<head>
<meta charset="utf-8">
<title>CuiFeng Enterprise Pte Ltd – Name Card</title>
<link rel="stylesheet" href="https://fonts.googleapis.com/css2?family=Gelasio:wght@400&display=swap">
<style>
  :root {
    --page-bg: #f4f4f4;
    --card-white: #ffffff;
    --card-grey: #c9c9c9;
    --brand-red: #f00a0a;
    --divider-red: #e8323a;
  }
  html, body {
    margin: 0;
    padding: 0;
    width: 1200px;
    height: 900px;
    overflow: hidden;
    background: var(--page-bg);
  }
  .canvas {
    position: relative;
    width: 1200px;
    height: 900px;
  }
  .card {
    position: absolute;
    left: 94px;
    top: 143px;
    width: 1012px;
    height: 613px;
    overflow: hidden;
    font-family: "Gelasio", Georgia, serif;
    color: var(--brand-red);
  }
  .card-surface {
    position: absolute;
    inset: 0;
  }
  .brand-mark {
    position: absolute;
    left: 68px;
    top: 73px;
    width: 133px;
    height: 134px;
    background: var(--brand-red);
  }
  .brand-name {
    position: absolute;
    left: 234px;
    top: 84px;
    margin: 0;
    font-weight: 400;
    line-height: 1;
  }
  .brand-name .primary {
    display: block;
    font-size: 84px;
    letter-spacing: 1px;
  }
  .brand-name .secondary {
    display: block;
    margin-top: 10px;
    margin-left: 8px;
    font-size: 30px;
    letter-spacing: 3px;
    text-transform: uppercase;
  }
  .person {
    position: absolute;
    right: 610px;
    top: 316px;
    text-align: right;
    font-size: 31px;
    line-height: 38px;
  }
  .person p { margin: 0; }
  .divider {
    position: absolute;
    left: 461px;
    top: 299px;
  }
  .contact {
    position: absolute;
    left: 518px;
    top: 322px;
    margin: 0;
    padding: 0;
    list-style: none;
    font-size: 31px;
    line-height: 56px;
    font-variant-numeric: oldstyle-nums;
  }
</style>
</head>
<body>
<main class="canvas">
  <section class="card" aria-label="CuiFeng Enterprise name card">
    <svg class="card-surface" width="1012" height="613" viewBox="0 0 1012 613" aria-hidden="true">
      <defs>
        <linearGradient id="surfaceShade" x1="0" y1="0" x2="1" y2="1">
          <stop offset="0.25" stop-color="var(--card-white)"/>
          <stop offset="1" stop-color="var(--card-grey)"/>
        </linearGradient>
        <linearGradient id="foldLight" x1="0" y1="0" x2="0.6" y2="1">
          <stop offset="0.5" stop-color="#ffffff" stop-opacity="1"/>
          <stop offset="1" stop-color="#ffffff" stop-opacity="0"/>
        </linearGradient>
      </defs>
      <rect width="1012" height="613" fill="url(#surfaceShade)"/>
      <polygon points="0,0 1012,0 456,335 386,279 0,613" fill="url(#foldLight)"/>
      <polygon points="0,0 1012,0 456,335 386,279 0,380" fill="#ffffff"/>
    </svg>

    <div class="brand-mark" aria-hidden="true"></div>
    <h1 class="brand-name">
      <span class="primary">CuiFeng</span>
      <span class="secondary">Enterprise Pte Ltd</span>
    </h1>

    <div class="person">
      <p class="person-name">Name Surename</p>
      <p class="person-title">Title</p>
    </div>

    <svg class="divider" width="8" height="246" viewBox="0 0 8 246" aria-hidden="true">
      <path d="M4 0 Q8 123 4 246 Q0 123 4 0 Z" fill="var(--divider-red)"/>
    </svg>

    <ul class="contact">
      <li>Address : Street, 123z</li>
      <li>Email : email@mail.com</li>
      <li>Tel : (123) 123-000-123</li>
      <li>Mobile : (123) 123-000-123</li>
    </ul>
  </section>
</main>
</body>
</html>
```